Using attached logo that has been created

Business card with logo that's attached. Maybe with water or the cartoon van in background. Looking for it to not be so plain and not too white.
Information to include;
Dario Whitlock
(555) 208-7713
Info@mossbrookpipeworks.example
www.mossbrookpipeworks.example
License # 5320417
Looking forward to the designs u come up with.
Thank you!
-Teresa
The designer (Brynn), that I would like to work with requested an extension to allow time to create a couple designs for this project.
Target Market(s)
Plumbing
Industry/Entity Type
Plumbing
Contact Information for Business Card
Listed above
Font styles to use
Look and feel

```html
<!DOCTYPE html>
<html lang="en">
<head>
<meta charset="utf-8">
<title>Mossbrook Pipeworks &amp; More – Business Card</title>
<link rel="stylesheet" href="https://fonts.googleapis.com/css2?family=Arvo:wght@400;700&family=Yellowtail&display=swap">
<style>
  :root {
    --bg: #9c9c9c;
    --card-white: #ffffff;
    --brand-blue: #1157a8;
    --brand-yellow: #ffc20e;
    --ink: #4a4a4a;
    --black: #111111;
    --figure-top: #2d6cc0;
    --figure-bottom: #8a7553;
  }
  * { box-sizing: border-box; margin: 0; padding: 0; }
  html, body { width: 1200px; height: 1200px; overflow: hidden; }
  body { background: var(--bg); position: relative; font-family: "Arvo", serif; }

  .card {
    position: absolute;
    left: 262px;
    width: 686px;
    height: 392px;
    border-radius: 22px;
    overflow: hidden;
  }
  .card--front { top: 165px; background: var(--card-white); }
  .card--back { top: 653px; background: var(--brand-yellow); }

  .front-swoosh { position: absolute; inset: 0; width: 100%; height: 100%; }

  .brand-name {
    position: absolute;
    left: 43px;
    top: 82px;
    width: 320px;
    font-family: "Arvo", serif;
    font-weight: 700;
    color: var(--brand-blue);
    font-size: 32px;
    line-height: 1.1;
  }
  .brand-name .brand-sub { display: block; font-size: 19px; }

  .contact {
    position: absolute;
    left: 43px;
    top: 238px;
    font-size: 14.5px;
    color: var(--ink);
    list-style: none;
  }
  .contact .license { margin-bottom: 12px; }
  .contact li { display: flex; align-items: center; gap: 9px; height: 20px; }
  .contact svg { width: 12px; height: 12px; fill: var(--brand-blue); flex: none; }

  .owner-name {
    position: absolute;
    right: 28px;
    bottom: 28px;
    font-family: "Yellowtail", cursive;
    font-size: 36px;
    color: #fff;
  }

  .mascot {
    position: absolute;
    left: 286px;
    top: 35px;
    width: 146px;
    height: 190px;
    border-radius: 40px 40px 10px 10px;
    background: linear-gradient(to bottom, var(--figure-top) 0%, var(--figure-top) 45%, var(--figure-bottom) 100%);
  }
  .brand-name--back {
    position: absolute;
    left: 0;
    right: 0;
    top: 236px;
    text-align: center;
    font-weight: 700;
    color: var(--brand-blue);
    font-size: 30px;
    line-height: 1.1;
  }
  .brand-name--back .brand-sub { display: block; font-size: 18px; }

  .back-url {
    position: absolute;
    left: 0;
    right: 0;
    top: 343px;
    text-align: center;
    font-size: 14px;
    letter-spacing: 0.55em;
    padding-left: 0.55em;
    color: var(--black);
  }
</style>
</head>
<body>

<section class="card card--front">
  <svg class="front-swoosh" viewBox="0 0 800 457" preserveAspectRatio="none" aria-hidden="true">
    <path d="M667,50 C650,250 480,400 252,457 L335,457 C540,390 668,220 671,0 L669,0 Z" fill="var(--brand-yellow)"/>
    <path d="M671,0 C668,220 540,390 335,457" fill="none" stroke="var(--black)" stroke-width="2.5"/>
    <path d="M732,0 L800,0 L800,457 L345,457 C560,380 712,230 732,0 Z" fill="var(--brand-blue)"/>
    <path d="M732,0 C712,230 560,380 345,457" fill="none" stroke="var(--black)" stroke-width="2.5"/>
  </svg>

  <div class="brand-name">Mossbrook Pipeworks<span class="brand-sub">&amp; More</span></div>

  <ul class="contact">
    <li class="license">License # 5320417</li>
    <li>
      <svg viewBox="0 0 24 24"><path d="M6.6 10.8a15.1 15.1 0 0 0 6.6 6.6l2.2-2.2a1 1 0 0 1 1-.25 11.4 11.4 0 0 0 3.6.57 1 1 0 0 1 1 1V20a1 1 0 0 1-1 1A17 17 0 0 1 3 4a1 1 0 0 1 1-1h3.5a1 1 0 0 1 1 1c0 1.25.2 2.45.57 3.6a1 1 0 0 1-.25 1z"/></svg>
      (555) 208-7713
    </li>
    <li>
      <svg viewBox="0 0 24 24"><path d="M2 5h20v14H2z M2 5l10 8 10-8" fill="var(--brand-blue)" stroke="#fff" stroke-width="1.5"/></svg>
      Info@mossbrookpipeworks.example
    </li>
    <li>
      <svg viewBox="0 0 24 24"><circle cx="12" cy="12" r="10"/><path d="M7 8c2 0 3 1 3 3s-2 2-2 4M15 5c-1 2 0 3 2 3M14 19c0-2 1-3 3-3" stroke="#fff" stroke-width="1.6" fill="none"/></svg>
      www.mossbrookpipeworks.example
    </li>
  </ul>

  <div class="owner-name">Dario Whitlock</div>
</section>

<section class="card card--back">
  <div class="mascot" role="img" aria-label="Cartoon illustration of the plumber holding a pipe wrench and a circular saw"></div>
  <div class="brand-name--back">Mossbrook Pipeworks<span class="brand-sub">&amp; More</span></div>
  <div class="back-url">WWW.MOSSBROOKPIPEWORKS.EXAMPLE</div>
</section>

</body>
</html>
```